Homepage design for personal injury lawyer

NOTE: I will not close the project until June 9th. I want to give everyone time to put in their best work.
Your task is to redesign the homepage for this site:
https://fennickharlow.com/
Feel free to use any images you find on the site.
I'm deliberately leaving the description simple so that I don't limit you.
Updates
Hi everyone. I will keep the project open for a few days to leave time for designs.
Need extra days to review
Number of Pages Required
1 page
Look and feel
Each slider illustrates characteristics of the customer's brand and the style your logo design should communicate.

```html
<!DOCTYPE html>
<html lang="en">
<head>
<meta charset="utf-8">
<title>Fennick Harlow – Phoenix Personal Injury Lawyers</title>
<link rel="stylesheet" href="https://fonts.googleapis.com/css2?family=Noto+Serif:ital,wght@0,700;1,400&family=Open+Sans:wght@400;600;700&family=Oswald:wght@500&display=swap">
<style>
  :root{
    --green:#3a7561;
    --blue:#3a72ae;
    --blue-soft:#8fb0d8;
    --ink-gray:#6a6a6a;
    --caption:#6e6e6e;
    --caption-faint:#c4c4c4;
    --white:#ffffff;
    --brand-gradient:linear-gradient(90deg,var(--green) 0%,var(--blue) 100%);
  }
  *{margin:0;padding:0;box-sizing:border-box}
  html,body{width:1200px;height:865px;overflow:hidden;background:var(--white)}
  body{position:relative;font-family:"Open Sans",sans-serif;color:var(--white)}

  .site-header{position:absolute;left:0;top:0;width:1200px;height:132px;background:var(--brand-gradient)}
  .brand{position:absolute;left:47px;top:54px;display:flex;align-items:center;gap:12px}
  .brand-dot{width:46px;height:46px;border-radius:50%;background:var(--white)}
  .brand-name{font-family:"Open Sans",sans-serif;font-weight:600;font-size:26px;color:var(--white);letter-spacing:.5px}

  .main-nav{position:absolute;left:435px;top:84px;display:flex;gap:0}
  .main-nav a{font-weight:700;font-size:14.5px;color:var(--white);text-decoration:none;display:flex;align-items:center;gap:4px}
  .main-nav a.has-menu::after{content:"";border-left:3px solid transparent;border-right:3px solid transparent;border-top:4px solid var(--white);margin-top:3px}
  .nav-about{margin-right:29px}
  .nav-cases{margin-right:30px}
  .nav-location{margin-right:29px}
  .nav-resources{margin-right:23px}

  .header-cta{position:absolute;left:985px;top:49px;width:189px;height:54px;border:2px solid var(--white);border-radius:28px;text-align:center;padding-top:7px}
  .header-cta .cta-label{display:block;font-weight:700;font-size:9px;line-height:12px}
  .header-cta .cta-phone{display:block;font-weight:700;font-size:21px;line-height:24px}

  .hero-title{position:absolute;left:0;top:173px;width:1200px;text-align:center;font-family:"Noto Serif",serif;font-weight:700;font-size:47px;line-height:60px;color:var(--green)}
  .hero-title .city{color:var(--blue)}
  .hero-lead{position:absolute;left:350px;top:244px;width:500px;text-align:center;font-size:11.5px;line-height:14px;color:var(--ink-gray)}

  .case-slider{position:absolute;left:0;top:318px;width:1200px;height:300px}
  .slide-caption{position:absolute;font-family:"Noto Serif",serif;font-style:italic;font-size:19px;color:var(--caption-faint);white-space:nowrap}
  .caption-prev{left:41px;top:14px}
  .caption-current{left:388px;top:1px;color:var(--caption)}
  .caption-next{right:33px;top:14px}
  .slide{position:absolute;border-radius:24px;overflow:hidden}
  .slide-prev{left:30px;top:48px;width:475px;height:246px;background:linear-gradient(90deg,#eef3fa 0%,var(--blue-soft) 45%,var(--blue) 100%);box-shadow:0 6px 10px rgba(0,0,0,.12)}
  .slide-next{left:705px;top:48px;width:475px;height:246px;background:linear-gradient(90deg,var(--blue) 0%,var(--blue-soft) 55%,#f1f5fb 100%);box-shadow:0 6px 10px rgba(0,0,0,.12)}
  .slide-current{left:361px;top:34px;width:478px;height:246px;background:linear-gradient(135deg,#9a9389 0%,#5a4a3e 45%,#c9a24a 75%,#6b5a48 100%);box-shadow:0 6px 12px rgba(0,0,0,.3);z-index:2}
  .slider-arrow{position:absolute;top:152px;width:38px;height:38px;border-radius:50%;background:var(--white);display:flex;align-items:center;justify-content:center;z-index:3}
  .arrow-prev{left:303px}
  .arrow-next{left:859px}

  .stats-band{position:absolute;left:0;top:727px;width:1200px;height:138px;background:var(--green)}
  .stats-list{position:absolute;left:0;top:0;width:847px;height:138px;background:var(--brand-gradient)}
  .stat{position:absolute;top:40px}
  .stat-1{left:45px}.stat-2{left:308px}.stat-3{left:569px}
  .stat-figure{font-family:"Noto Serif",serif;font-weight:700;font-size:32px;line-height:40px}
  .stat-label{font-family:"Oswald",sans-serif;font-weight:500;font-size:14px;text-transform:uppercase;margin-left:6px}
  .stat-note{font-size:11px;line-height:14px;margin-top:-2px}
  .band-cta{position:absolute;left:896px;top:32px;width:271px;height:74px;border:2px solid var(--white);border-radius:12px;padding:10px 0 0 18px}
  .band-cta .cta-label{display:block;font-weight:600;font-size:13px;line-height:16px}
  .band-cta .cta-phone{display:block;font-family:"Noto Serif",serif;font-weight:700;font-size:30px;line-height:38px}
</style>
</head>
<body>
  <header class="site-header">
    <a class="brand" href="https://fennickharlow.com/" aria-label="Fennick Harlow home">
      <span class="brand-dot"></span>
      <span class="brand-name">Fennick Harlow</span>
    </a>
    <nav class="main-nav">
      <a class="nav-about has-menu" href="#">About Us</a>
      <a class="nav-cases has-menu" href="#">Case We Handle</a>
      <a class="nav-location has-menu" href="#">Location</a>
      <a class="nav-resources has-menu" href="#">Resources</a>
      <a class="nav-contact" href="#">Contact Us</a>
    </nav>
    <div class="header-cta">
      <span class="cta-label">Call 24/7 for Free Consultation</span>
      <span class="cta-phone">602-555-0148</span>
    </div>
  </header>

  <h1 class="hero-title"><span class="city">Phoenix</span> Personal Injury Lawyers</h1>
  <p class="hero-lead">Our experienced team of attorneys provides personalized legal solutions with a commitment to excellence and client satisfaction.</p>

  <section class="case-slider">
    <span class="slide-caption caption-prev">Lorem Ipsum Dolor</span>
    <span class="slide-caption caption-current">Lorem Ipsum Dolor</span>
    <span class="slide-caption caption-next">Lorem Ipsum Dolor</span>
    <div class="slide slide-prev" role="img" aria-label="Photo of clients meeting with an attorney at a table, blue tint"></div>
    <div class="slide slide-current" role="img" aria-label="Photo of a couple in consultation with an attorney in an office"></div>
    <div class="slide slide-next" role="img" aria-label="Photo of an attorney explaining a case in an office, blue tint"></div>
    <span class="slider-arrow arrow-prev"><svg width="14" height="18" viewBox="0 0 14 18"><path d="M11 1 L2 9 L11 17 Z" fill="#3a72ae"/></svg></span>
    <span class="slider-arrow arrow-next"><svg width="14" height="18" viewBox="0 0 14 18"><path d="M3 1 L12 9 L3 17 Z" fill="#3a72ae"/></svg></span>
  </section>

  <section class="stats-band">
    <div class="stats-list">
      <div class="stat stat-1">
        <div class="stat-figure">99%<span class="stat-label">Success Rate</span></div>
        <p class="stat-note">Lorem ipsum dolor sit amet, consectetuer</p>
      </div>
      <div class="stat stat-2">
        <div class="stat-figure">550+<span class="stat-label">5-Star Reviews</span></div>
        <p class="stat-note">Lorem ipsum dolor sit amet, consectetuer</p>
      </div>
      <div class="stat stat-3">
        <div class="stat-figure">$0 Fee</div>
        <p class="stat-note">Lorem ipsum dolor sit amet, consectetuer</p>
      </div>
    </div>
    <div class="band-cta">
      <span class="cta-label">Call 24/7 for Free Consultation</span>
      <span class="cta-phone">602-555-0148</span>
    </div>
  </section>
</body>
</html>
```